Brevinor
Brevinor - Consulting
Use same font as used in my logo
It is up to you.
Simple
Lionel Brasquet
President
82 Thornwell Avenue Toronto, Ontario M4R 2J8
l.brasquet@brevinorhub.com
www.brevinorhub.com
Will be the same however in French

```html
<!DOCTYPE html>
<html lang="en">
<head>
<meta charset="utf-8">
<title>Brevinor – Business Card Set</title>
<link href="https://fonts.googleapis.com/css2?family=Arimo:wght@400;700&display=swap" rel="stylesheet">
<style>
  :root {
    --stage: #0b0b0b;
    --card-edge: #b9bcc2;
    --white: #ffffff;
    --navy-deep: #153560;
    --navy-light: #3a6392;
    --navy-text: #1f4576;
    --grey-card: #58595d;
    --grey-card-light: #66676b;
    --swoosh-grey: #8a8d93;
    --muted: #3a3a3a;
  }
  * { box-sizing: border-box; margin: 0; padding: 0; }
  html, body {
    width: 1200px; height: 670px; overflow: hidden;
    background: var(--stage);
    font-family: "Arimo", Arial, sans-serif;
  }
  .sheet { position: relative; width: 1200px; height: 670px; }
  .card {
    position: absolute;
    width: 492px; height: 274px;
    border-radius: 30px;
    border: 2px solid var(--card-edge);
    overflow: hidden;
  }
  .card--front { left: 91px; top: 41px; background: var(--white); }
  .card--back-blue {
    left: 606px; top: 41px;
    background: linear-gradient(90deg, var(--navy-deep), var(--navy-light));
  }
  .card--back-white { left: 91px; top: 341px; background: var(--white); }
  .card--back-grey {
    left: 606px; top: 341px;
    background: linear-gradient(90deg, var(--grey-card), var(--grey-card-light));
  }

  .brand-name {
    font-family: "Arimo", Arial, sans-serif;
    font-weight: 700;
    letter-spacing: 3px;
    text-transform: uppercase;
  }
  .card--front .brand-name {
    position: absolute; left: 30px; top: 20px;
    font-size: 30px; color: var(--navy-text);
  }
  .card--back-blue .brand-name,
  .card--back-white .brand-name,
  .card--back-grey .brand-name {
    position: absolute; left: 0; right: 0; top: 50%;
    transform: translateY(-50%);
    text-align: center; font-size: 40px;
  }
  .card--back-blue .brand-name,
  .card--back-grey .brand-name { color: var(--white); }
  .card--back-white .brand-name { color: var(--navy-text); }

  .identity {
    position: absolute; left: 136px; width: 200px; top: 98px;
    text-align: center;
  }
  .identity__name { font-size: 22px; font-weight: 700; color: var(--navy-text); line-height: 26px; }
  .identity__title { font-size: 12px; color: var(--muted); line-height: 14px; margin-top: 2px; }

  .front-band { position: absolute; left: 0; top: 0; width: 492px; height: 274px; }

  .contact {
    position: absolute; left: 14px; top: 190px;
    color: var(--white); font-size: 12px; line-height: 15px;
    list-style: none;
  }
</style>
</head>
<body>
<main class="sheet">
  <section class="card card--front" aria-label="Card front">
    <svg class="front-band" viewBox="0 0 492 274" aria-hidden="true">
      <defs>
        <linearGradient id="bandFill" x1="0" y1="0" x2="1" y2="0">
          <stop offset="0" stop-color="#153560"/>
          <stop offset="1" stop-color="#3a6392"/>
        </linearGradient>
      </defs>
      <path d="M0 180 Q300 172 492 115 L492 274 L0 274 Z" fill="url(#bandFill)"/>
      <path d="M0 180 Q300 172 492 115 L492 104 Q300 160 0 170 Z" fill="#8a8d93"/>
    </svg>
    <div class="brand-name">Brevinor</div>
    <div class="identity">
      <div class="identity__name">Lionel Brasquet</div>
      <div class="identity__title">President</div>
    </div>
    <ul class="contact">
      <li>82 Thornwell Avenue</li>
      <li>Toronto, Ontario, M4R 2J8</li>
      <li>Cell: (416) 555-0183</li>
      <li>Email: l.brasquet@brevinorhub.com</li>
      <li>www.brevinorhub.com</li>
    </ul>
  </section>

  <section class="card card--back-blue" aria-label="Card back, blue">
    <div class="brand-name">Brevinor</div>
  </section>

  <section class="card card--back-white" aria-label="Card back, white">
    <div class="brand-name">Brevinor</div>
  </section>

  <section class="card card--back-grey" aria-label="Card back, grey">
    <div class="brand-name">Brevinor</div>
  </section>
</main>
</body>
</html>
```